Renamed Motel Needs Appealing Flyer

We need a flyer design for a motel that has been closed for 3 years and has just reopened under new management. It has been renamed 'Tallowind Motel' and is located in the Grampians in Vic. We would like our design to showcase the beauty and magnificence of the Grampians National Park (Gariwerd being the Aboriginal name for the Park). The motel is an older style building, so we don't want photos of the building to be the focus of the flyer until we have had time to renovate etc.
http://www.filedrovex.com/file/9tq2pm
I will add a high res image of the motel name/logo on Monday
http://www.filedrovex.com/file/9tq2pm to see an additional photo. I will add a high res image of motel name/logo on Monday
all ages, backpackers, budget consious travellers, seniors, groups
- Flyer must be DL size (front and back only) with logo at the top so that it is visible when displayed in a tiered display rack. I am not sure if the logo I have provided is adequate resolution wise. Can you let me know if it is not? The 'points' under the name are not part of the logo and should be removed.
Suggested wording for front of flyer - Surrounded by rugged mountain ranges and native plants and animals, Tallowind Motel is the perfect base to explore the natural beauty of the Grampians.
Back of flyer - features: affordable accommodation, 25 spacious ground floor rooms,
single/twin/triple/quadruple rooms; queen beds; ensuite bathrooms/some rooms with baths; toaster/ tea and coffee making facilities; iron/ironing board in rooms; digital TV; free WiFi; microwaves for guest use; free BBQ facilities; breakfast available; conference facility for up to 25 persons
Address - 14 Brackley Rd, Mossvale 3274
Phone: (03) 5471 2098
Email: tallowindmotel@quokmail.com
www.tallowindmotel.com.au
Updated after first set of submissions/comments - 10.55 PM AEST.
The following text only should be for the front of the brochure - Surrounded by rugged mountain ranges and native plants and animals, Tallowind Motel is the perfect base to explore the natural beauty of the Grampians.
Logically then, listings from the original brief such as 'Surrounded by mountains' would not be relevant for the back.
The dot points listed above in the first brief, should then be the focus for the information and detail on the back of the brochure.
Another update is;
- correct display is R/Trak
- I would like the flyer to have a flowing feel, print over top of scenery images, different fonts. Perhaps back of flyer could be printed over a washed image of Grampians

```html
<!DOCTYPE html>
<html lang="en">
<head>
<meta charset="utf-8">
<title>Tallowind Motel – DL Flyer</title>
<link href="https://fonts.googleapis.com/css2?family=Carlito:ital,wght@0,400;0,700;1,700&family=Noto+Sans:wght@400;700&family=Open+Sans:wght@400;700&display=swap" rel="stylesheet">
<style>
  :root{
    --page:#ffffff;
    --label:#333333;
    --front-green:#1e4a2c;
    --back-green:#163f26;
    --cream:#f6ebb4;
    --white:#ffffff;
    --row-bright:#0b5a33;
    --row-dark:#0e2d1a;
    --frame:#ffffff;
  }
  *{box-sizing:border-box;margin:0;padding:0}
  html,body{width:1200px;height:900px;overflow:hidden;background:var(--page)}
  body{position:relative;font-family:"Open Sans",sans-serif}
  .side-label{position:absolute;top:38px;width:120px;text-align:center;font-size:12px;color:var(--label);letter-spacing:.3px}
  .side-label.front{left:337px}
  .side-label.back{left:794px}

  .panel{position:absolute;overflow:hidden}
  .panel.front{left:234px;top:82px;width:350px;height:743px;background:var(--front-green)}
  .panel.back{left:664px;top:78px;width:351px;height:744px;background:var(--back-green)}

  .brand{position:absolute;left:0;width:100%;text-align:center;font-family:"Open Sans",sans-serif;font-weight:700;font-size:38px;line-height:1;color:var(--cream);letter-spacing:-.5px}
  .front .brand{top:30px}
  .back .brand{top:30px}

  .front-intro{position:absolute;left:68px;top:123px;width:232px;color:var(--white);font-family:"Carlito",sans-serif;font-weight:700;font-size:13.4px;line-height:17px}

  .photo{position:absolute;background:var(--frame);padding:6px;box-shadow:1px 2px 4px rgba(0,0,0,.4)}
  .photo .shot{width:100%;height:100%}
  .photo.cliffs{left:86px;top:240px;width:186px;height:136px;transform:rotate(5deg)}
  .photo.cliffs .shot{background:linear-gradient(180deg,#f2e6c8 0%,#c7b489 30%,#9a7a36 55%,#5a5a2a 100%)}
  .photo.valley{left:38px;top:390px;width:190px;height:120px;transform:rotate(-19deg)}
  .photo.valley .shot{background:linear-gradient(180deg,#8fb4de 0%,#c2d4e6 30%,#5d7a66 55%,#3a5a2a 100%)}
  .photo.building{left:140px;top:446px;width:178px;height:116px;transform:rotate(-20deg)}
  .photo.building .shot{background:linear-gradient(90deg,#6d5a3c 0%,#e8dcc0 35%,#c9bd9e 55%,#3b3f2e 80%,#7d8a8c 100%)}
  .photo.room{left:66px;top:540px;width:176px;height:132px;transform:rotate(4deg)}
  .photo.room .shot{background:linear-gradient(180deg,#d8d6cf 0%,#b6b3a8 45%,#5f84a0 70%,#3a3e4a 100%)}

  .front-rule{position:absolute;left:67px;top:705px;width:213px;height:2px;background:var(--cream)}

  .contact{position:absolute;left:67px;top:106px;color:var(--cream);font-family:"Noto Sans",sans-serif;font-weight:700;font-size:12.2px;line-height:13.5px}
  .contact .gap{margin-top:13px}

  .features{position:absolute;left:60px;top:177px;list-style:none;color:var(--white);font-family:"Noto Sans",sans-serif;font-size:11.2px;line-height:13.5px}
  .features li{padding-left:13px;position:relative}
  .features li::before{content:"";position:absolute;left:2px;top:6px;width:3px;height:3px;border-radius:50%;background:var(--white)}

  .coach-title{position:absolute;left:0;width:100%;top:330px;text-align:center;color:var(--cream);font-family:"Carlito",sans-serif;font-weight:700;font-style:italic;font-size:18px}

  .timetable{position:absolute;left:40px;width:260px;border-collapse:collapse;font-family:"Carlito",sans-serif;font-size:9.6px;color:var(--white);table-layout:fixed}
  .timetable.outward{top:358px}
  .timetable.return{top:528px}
  .timetable td,.timetable th{height:12px;line-height:12px;padding:0 0 0 6px;text-align:left;font-weight:400;white-space:nowrap;overflow:hidden}
  .timetable .section th,.timetable .heads th{color:var(--cream)}
  .timetable col.c1{width:65px}
  .timetable col.c2{width:87px}
  .timetable col.c3{width:53px}
  .timetable col.c4{width:55px}
  .timetable td:nth-child(3),.timetable th:nth-child(3){padding-left:0}
  .timetable td:nth-child(4),.timetable th:nth-child(4){padding-left:1px}
  .timetable td[colspan]{padding-left:6px}
  .timetable .bright td{background:var(--row-bright)}
  .timetable .dark td{background:var(--row-dark)}
</style>
</head>
<body>
  <div class="side-label front">FRONT</div>
  <div class="side-label back">BACK</div>

  <section class="panel front">
    <header class="brand">Tallowind Motel</header>

    <p class="front-intro">Surrounded by rugged mountain ranges and native plants and animals, Tallowind Motel is the perfect base to explore the natural beauty of the Grampians.</p>

    <figure class="photo cliffs"><div class="shot" role="img" aria-label="Sunlit sandstone cliffs of the Grampians ranges"></div></figure>
    <figure class="photo valley"><div class="shot" role="img" aria-label="View over forested Grampians valleys and ridges"></div></figure>
    <figure class="photo building"><div class="shot" role="img" aria-label="Motel entrance sign on a rendered wall with a parked car"></div></figure>
    <figure class="photo room"><div class="shot" role="img" aria-label="Motel twin room with two made beds"></div></figure>

    <div class="front-rule"></div>
  </section>

  <section class="panel back">
    <header class="brand">Tallowind Motel</header>

    <div class="contact">
      <p>14 Brackley Rd, Mossvale 3274</p>
      <p>phone: (03) 5471 2098</p>
      <p class="gap">email: tallowindmotel@quokmail.com</p>
      <p>website: tallowindmotel.com.au</p>
    </div>

    <ul class="features">
      <li>Single/twin/triple/quadruple rooms</li>
      <li>Queen beds</li>
      <li>Ensuite bathrooms / some rooms with baths</li>
      <li>Toaster/tea and coffee making facilities</li>
      <li>Iron/ironing board in rooms</li>
      <li>Digital TV</li>
      <li>Free WiFi</li>
      <li>Microwaves for guests use;</li>
      <li>Free BBQ facilities</li>
      <li>Breakfast available</li>
      <li>Conference facility for up to 25 persons</li>
    </ul>

    <h2 class="coach-title">R/Trak Coach (Off-peak)</h2>

    <table class="timetable outward">
      <colgroup><col class="c1"><col class="c2"><col class="c3"><col class="c4"></colgroup>
      <tr class="section"><th colspan="4" style="padding-left:6px">OUTWARD JOURNEY</th></tr>
      <tr class="heads"><th>Depart</th><th>Arrive</th><th>Duration</th><th>Total Time</th></tr>
      <tr class="bright"><td colspan="4">Melbourne, Southern Cross to Ararat Station</td></tr>
      <tr class="bright"><td>08:28</td><td>11:57</td><td>3 h 29 min</td><td></td></tr>
      <tr class="bright"><td colspan="4">Ararat Station to Stawell Station</td></tr>
      <tr class="bright"><td>12:00</td><td>12:10</td><td>10 min</td><td></td></tr>
      <tr class="bright"><td colspan="4">Stawell Station to Mossvale</td></tr>
      <tr class="bright"><td>12:15</td><td>12:35</td><td>20 min</td><td>4 h 7 min</td></tr>
      <tr class="dark"><td colspan="4">Melbourne, Southern Cross to Ararat Station</td></tr>
      <tr class="dark"><td>08:28</td><td>11:57</td><td>3 h 29 min</td><td></td></tr>
      <tr class="dark"><td colspan="4">Wait at Ararat Station 3 hr 3 min</td></tr>
      <tr class="dark"><td colspan="4">Ararat Station to&nbsp; Mossvale</td></tr>
      <tr class="dark"><td>15:00</td><td>15:39</td><td>39 min</td><td>7 hr 11 min</td></tr>
    </table>

    <table class="timetable return">
      <colgroup><col class="c1"><col class="c2"><col class="c3"><col class="c4"></colgroup>
      <tr class="section"><th colspan="4" style="padding-left:6px">RETURN JOURNEY</th></tr>
      <tr class="heads"><th>Depart</th><th>Arrive</th><th>Duration</th><th>Total Time</th></tr>
      <tr class="bright"><td colspan="4">Mossvale to Ararat Station</td></tr>
      <tr class="bright"><td>10:46</td><td>11:25</td><td>39 min</td><td></td></tr>
      <tr class="bright"><td colspan="4">Wait at Ararat Station for 4 hr 40 min</td></tr>
      <tr class="bright"><td colspan="4">Ararat Station to Melbourne, Southern Cross</td></tr>
      <tr class="bright"><td>16:05</td><td>19:31</td><td>3 hr 16 min</td><td>8 hr 45 min</td></tr>
      <tr class="dark"><td colspan="4">Mossvale to Stawell Station</td></tr>
      <tr class="dark"><td>14:30</td><td>15:05</td><td>35 min</td><td></td></tr>
      <tr class="dark"><td colspan="4">Wait at Stawell Station for 8 min</td></tr>
      <tr class="dark"><td colspan="4">Stawell station to Ararat Station</td></tr>
      <tr class="dark"><td>15:13</td><td>15:47</td><td>34 min</td><td></td></tr>
      <tr class="dark"><td colspan="4">Wait at Ararat for 18 min</td></tr>
      <tr class="dark"><td colspan="4">Ararat Station to Melbourne, Southern Cross</td></tr>
      <tr class="dark"><td>16:05</td><td>19:31</td><td>3 hr 26 min</td><td>5 hr 1 min</td></tr>
    </table>
  </section>
</body>
</html>
```